Book Cover Design Project

I need a book cover design with the title

"Gilded Ledger - A Probe into Avarice and Graft in Australia’s $1 Trillion Retirement Savings Sector"

With a question on the cover of "How much of your superannuation has been stolen? Read this Book to Find Out"

The design should have money and greed based theme such as "$" for "S" in "Super"

Target Market(s)

Members of Superannuation (Pension) funds

Industry/Entity Type

Industry

Requirements
Must have
• Must have a money and greed theme

```html
<!DOCTYPE html>
<html lang="en">
<head>
<meta charset="UTF-8">
<title>Gilded Ledger – Book Cover</title>
<link rel="stylesheet" href="https://fonts.googleapis.com/css2?family=Archivo:wght@400;700;800;900&family=Archivo+Black&display=swap">
<style>
  :root {
    --page-bg: #f2f2f2;
    --cover-bg: #262626;
    --white: #ffffff;
    --grey-title: #8c8c8c;
    --grey-words: #4a4a4a;
    --red: #e8202a;
    --sign-red: #e21d24;
  }
  * { margin: 0; padding: 0; box-sizing: border-box; }
  html, body {
    width: 1200px;
    height: 900px;
    overflow: hidden;
    background: var(--page-bg);
  }
  .stage {
    width: 1200px;
    height: 900px;
    display: flex;
    align-items: center;
    justify-content: center;
  }
  .cover {
    position: relative;
    width: 600px;
    height: 830px;
    background: var(--cover-bg);
    font-family: "Archivo", Arial, sans-serif;
    color: var(--white);
    overflow: hidden;
  }
  .word-cloud {
    position: absolute;
    left: 34px;
    top: 34px;
    width: 536px;
    font-size: 17px;
    line-height: 22px;
    color: var(--grey-words);
    font-weight: 400;
  }
  .word-cloud .lead { color: var(--red); font-weight: 700; }
  .title {
    position: absolute;
    left: 30px;
    top: 176px;
    font-family: "Archivo Black", "Arial Black", sans-serif;
    font-size: 112px;
    line-height: 100px;
    letter-spacing: -3px;
    text-transform: uppercase;
  }
  .title .line-one { display: block; color: var(--white); }
  .title .line-one .accent { color: var(--red); }
  .title .line-two { display: block; color: var(--grey-title); }
  .subtitle {
    position: absolute;
    left: 34px;
    top: 402px;
    width: 360px;
    font-weight: 800;
  }
  .subtitle .probe { font-size: 25px; line-height: 28px; }
  .subtitle .amount { display: block; font-size: 46px; line-height: 48px; font-weight: 900; margin-top: 2px; }
  .subtitle .sector { display: block; font-size: 21px; line-height: 22px; font-weight: 700; }
  .author {
    position: absolute;
    left: 34px;
    top: 536px;
    font-size: 22px;
    font-weight: 800;
    color: var(--red);
    text-transform: uppercase;
  }
  .warning-sign {
    position: absolute;
    left: 396px;
    top: 424px;
    width: 172px;
    height: 152px;
  }
  .teaser {
    position: absolute;
    left: 34px;
    top: 676px;
    width: 270px;
    font-size: 14px;
    line-height: 19px;
    color: var(--white);
  }
  .teaser p + p { margin-top: 12px; }
</style>
</head>
<body>
<main class="stage">
  <article class="cover">
    <p class="word-cloud"><span class="lead">Fraud:</span> Kickbacks, Embezzlement, Bribery, Skimming, Cronyism, Collusion, Deceit, Theft, Rorting, Laundering, Insider Deals, Hidden Fees, Conflicts, Misconduct, Secrecy, Bonuses, Payouts, Schemes, Avarice, Graft, Plunder, Looting, Gouging, Exploitation, Swindling, Racketeering, Extortion, Cover-ups, Lobbying, Profiteering, Overcharging, Manipulation, Negligence, Opacity, Greed.</p>

    <h1 class="title">
      <span class="line-one"><span class="accent">G</span>ILDED</span>
      <span class="line-two">LEDGER</span>
    </h1>

    <h2 class="subtitle">
      <span class="probe">A Probe into Avarice &amp; Graft in Australia’s</span>
      <span class="amount">$1 trillion</span>
      <span class="sector">retirement savings sector</span>
    </h2>

    <p class="author">Author Name Goes Here</p>

    <svg class="warning-sign" viewBox="0 0 172 152" aria-label="Warning sign">
      <path d="M86 8 L166 144 L6 144 Z" fill="var(--white)" stroke="var(--sign-red)" stroke-width="14" stroke-linejoin="round"/>
      <rect x="78" y="56" width="16" height="52" rx="4" fill="#111"/>
      <circle cx="86" cy="123" r="9" fill="#111"/>
    </svg>

    <div class="teaser">
      <p>How much of your superannuation has been stolen?</p>
      <p>Read this book to find out.</p>
    </div>
  </article>
</main>
</body>
</html>
```